Vornelle Distance Learning Website

Vornelle provide e-learning and mixed learning solutions for individuals, colleges, organisations and B2B.
We need a modern, light and flat website design for Vornelle. We want to to see the designer incorporate user experience(UX) design elements into the AI or PSD mockups. We would like to see designs that use pastel colors that compliment yellow and black of our logo.
We want our E-learning experience to accelerate learning and for the interface to be user friendly and intuitive. We want the designs to focus on quick access to course information, course reviews, learning progress and study advice. Quick and intuitive access to all content for our clients is one of our top priorities.
We would like designs for the following project 3 pages:
1. Learner homepage dashboard (see attached screenshot).
On this page the Learners need to:
- Login
- Have quick access to Packages and Courses.
- See other recommended courses (Below Packages and Courses)
- Possibly a left hand side column/menu with thumbnail icons (See quillory learner dashboard screenshot)
2. Homepage
See current sample
http://www.vornelle-learn.test
We would like the designer to focus on creating a customized banner to enhance the home page.
3. Primary Landing/Marketing page
This page is geared towards customer acquisition with the focal point being the top banner (video or HD image).
And Course Preview content below.
See reference
http://vornelle-learn.test/subscriptionPlans/marketing/MTc%3D/Mjc4Nw%3D%3D/Mastering%20Dorvish%20%2B%20Dorvish%20Nibbles%20Bundle%20by%20Gideon%20Pell%20Mawry
Other site we like:
- https://www.brenvato.test (We like the home page and top bar on courses page)
- http://www.pollenhallstudy.test
- http://crestfoldlabs.test (think this site looks great, love the lower graphics on the homepage)
Updates
Hello,
Thank you for taking the time to contribute to this web design competition. We would just like to point out a few things:
1. Please try to make the color palette similar to the colors used in the screenshot that we just uploaded ('possible color palette).
2. Please make the designs specific to each page: THE LEARNER HOMEPAGE, HOME PAGE, and the MARKETING LANDING PAGE.
We are very happy with the high quality of designs so far,
Cheers,
Len Fa
KV-Studio
Also,
Please avoid using dark/bold elements in the designs. The ONLY elements that we want to be dark are the logo and the footer.
Any questions please ask,
Cheers,
Len Fa
Kv-Studio
Hello,
Based on the round of feedback we just gave it would be great if you could complete further design changes by tomorrow, as we are pushed for time.
Thank you,
Len Fa
KV-Studio

```html
<!DOCTYPE html>
<html lang="en">
<head>
<meta charset="utf-8">
<title>Vornelle – Distance Learning</title>
<link rel="stylesheet" href="https://fonts.googleapis.com/css2?family=Open+Sans:wght@400;600&family=Roboto+Condensed:wght@400;700&display=swap">
<style>
:root{
  --yellow:#f6bd1d;
  --yellow-deep:#d99a05;
  --ink:#1a1a1a;
  --text:#3c3c3c;
  --soft-text:#4a4440;
  --page:#f3f2f0;
  --band:#ededed;
  --footer:#1d1d1d;
  --white:#ffffff;
  --line:#b9b1aa;
}
*{box-sizing:border-box;margin:0;padding:0}
html,body{width:1200px;height:2381px;overflow:hidden}
body{font-family:"Open Sans",Arial,sans-serif;color:var(--text);background:var(--page);position:relative}

/* hero */
.hero{position:absolute;left:0;top:0;width:1200px;height:673px;overflow:hidden}
.hero-photo{position:absolute;inset:0;background:
  radial-gradient(ellipse 380px 420px at 870px 300px,#f3e1d6 0%,#ead8cc 45%,transparent 75%),
  radial-gradient(ellipse 300px 300px at 260px 260px,#e4dcd4,transparent 70%),
  linear-gradient(135deg,#e6ddd6 0%,#efe7e0 40%,#e2d8d0 70%,#e8e0da 100%)}
.hero-veil{position:absolute;inset:0;background:rgba(255,252,248,.35)}
.logo{position:absolute;left:156px;top:38px;display:flex;align-items:center;gap:10px}
.logo-dot{width:40px;height:40px;border-radius:50%;background:var(--yellow)}
.logo-name{font-weight:600;font-size:34px;color:var(--ink);letter-spacing:-.5px}
.account{position:absolute;left:884px;top:20px;display:flex;align-items:center;gap:12px;color:var(--ink);font-size:14px;font-weight:600}
.account-icon{width:30px;height:30px;border:2px solid var(--yellow);display:flex;align-items:center;justify-content:center;background:var(--white)}
.account .sep{color:#777}
.nav{position:absolute;left:452px;top:81px;display:flex;height:25px}
.nav a{color:var(--ink);text-decoration:none;font-size:12px;letter-spacing:.4px;line-height:25px;padding:0 11px;white-space:nowrap}
.nav a.is-active{background:var(--yellow)}
.search-toggle{position:absolute;left:1014px;top:81px;width:29px;height:26px;background:var(--yellow);display:flex;align-items:center;justify-content:center}
.search-box{position:absolute;left:821px;top:107px;width:222px;height:36px;border:3px solid var(--yellow);background:var(--white);display:flex;align-items:center;padding:0 4px 0 8px;gap:6px}
.search-box span{flex:1;font-size:11px;font-style:italic;color:#888}
.search-box b{background:var(--yellow);color:var(--ink);font-size:11px;font-weight:600;padding:3px 8px}

.video{position:absolute;left:156px;top:270px;width:498px;height:274px;border:4px solid var(--white);background:var(--white);box-shadow:0 4px 14px rgba(0,0,0,.18)}
.video-frame{position:absolute;left:0;top:0;width:490px;height:238px;background:linear-gradient(90deg,#f0f0f0 0%,#e2dcd8 20%,#c88f7c 32%,#e9e6e4 48%,#f6f6f6 62%,#f6e08a 85%,#f7f7f7 100%)}
.video-bar{position:absolute;left:0;top:238px;width:490px;height:28px;background:#161616;display:flex;align-items:center;gap:10px;padding:0 10px;color:#ddd;font-size:10px}
.video-track{position:relative;flex:1;height:4px;background:#555;border-radius:2px}
.video-track i{position:absolute;left:0;top:0;width:12%;height:4px;background:#ccc}
.video-track b{position:absolute;left:11%;top:-4px;width:12px;height:12px;border-radius:50%;background:#eee}

.promo{position:absolute;left:706px;top:282px;color:var(--ink)}
.promo h1{font-family:"Roboto Condensed",sans-serif;font-weight:700;font-size:60px;color:var(--yellow-deep);line-height:1;letter-spacing:.5px}
.promo p{font-family:"Roboto Condensed",sans-serif;font-size:29px;line-height:35px;margin-top:28px;width:480px}
.btn-start{position:absolute;left:708px;top:492px;width:151px;height:40px;background:var(--yellow);color:var(--ink);font-family:"Roboto Condensed",sans-serif;font-weight:700;font-size:17px;display:flex;align-items:center;justify-content:center;gap:8px}

/* features */
.feature-title{position:absolute;font-family:"Roboto Condensed",sans-serif;font-weight:400;font-size:27px;color:var(--ink);letter-spacing:.2px}
.feature-text{position:absolute;width:590px;font-size:12.4px;line-height:22px;color:#444}
.feature-art{position:absolute;width:243px;height:243px;border-radius:50%}

/* contact */
.contact{position:absolute;left:0;top:1781px;width:1200px;height:430px;overflow:hidden}
.contact-photo{position:absolute;inset:0;background:
  radial-gradient(ellipse 320px 260px at 640px 250px,#f2dde0,transparent 70%),
  linear-gradient(120deg,#e9e4e0 0%,#efe9e6 50%,#e6e0dc 100%)}
.contact-veil{position:absolute;inset:0;background:rgba(255,255,255,.35)}
.contact h2{position:absolute;left:0;width:1200px;top:26px;text-align:center;font-weight:400;font-size:18px;color:var(--yellow-deep)}
.contact-rule{position:absolute;left:527px;top:58px;width:146px;height:2px;background:var(--yellow)}
.field{position:absolute;border-bottom:1px solid var(--line);color:var(--soft-text);font-size:12px;padding:0 0 8px 18px}
.message{position:absolute;left:156px;top:194px;width:888px;height:141px;border:1px solid var(--line);color:var(--soft-text);font-size:12px;padding:16px 18px}
.btn-send{position:absolute;left:552px;top:356px;width:94px;height:38px;background:var(--yellow);color:var(--white);font-size:18px;display:flex;align-items:center;justify-content:center;letter-spacing:.5px}

/* newsletter */
.newsletter{position:absolute;left:0;top:2211px;width:1200px;height:99px;background:var(--band)}
.newsletter h3{position:absolute;left:156px;top:29px;font-weight:400;font-size:17px;color:#444}
.newsletter p{position:absolute;left:156px;top:57px;font-size:14px;color:#555}
.newsletter p a{color:var(--yellow);text-decoration:none}
.news-input{position:absolute;left:667px;top:27px;width:255px;height:43px;background:var(--white);font-size:12px;color:#666;padding:14px 16px}
.news-btn{position:absolute;left:922px;top:27px;width:121px;height:43px;background:var(--yellow);color:var(--white);font-size:15px;display:flex;align-items:center;justify-content:center}

/* footer */
.footer{position:absolute;left:0;top:2310px;width:1200px;height:71px;background:var(--footer)}
.footer-links{position:absolute;left:156px;top:16px;font-size:12px;color:#bbb}
.footer-links a{color:#bbb;text-decoration:none}
.footer-links a.is-active{color:var(--yellow)}
.footer-links .sep{margin:0 6px;color:#777}
.copyright{position:absolute;left:156px;top:44px;font-size:11px;color:#999}
.copyright b{color:var(--yellow);font-weight:400}
.social{position:absolute;left:826px;top:17px;display:flex;gap:14px}
.social span{width:33px;height:33px;border-radius:50%;border:2px solid #777}
.social span.is-active{background:var(--yellow);border-color:var(--yellow)}
</style>
</head>
<body>

<header class="hero">
  <div class="hero-photo" role="img" aria-label="Smiling student holding a tablet among classmates in a library"></div>
  <div class="hero-veil"></div>

  <div class="logo"><span class="logo-dot"></span><span class="logo-name">Vornelle</span></div>

  <div class="account">
    <span class="account-icon">
      <svg width="14" height="14" viewBox="0 0 14 14"><circle cx="7" cy="4.5" r="3" fill="#f6bd1d"/><path d="M1 14c0-4 3-5.5 6-5.5s6 1.5 6 5.5z" fill="#f6bd1d"/></svg>
    </span>
    <span>Login</span><span class="sep">|</span><span>Register</span>
  </div>

  <nav class="nav">
    <a class="is-active" href="#">HOME</a>
    <a href="#">ABOUT</a>
    <a href="#">EVENTS</a>
    <a href="#">ADMISSIONS</a>
    <a href="#">COURSES</a>
    <a href="#">STAFF</a>
    <a href="#">CONTACT</a>
  </nav>
  <div class="search-toggle">
    <svg width="15" height="15" viewBox="0 0 15 15"><circle cx="6" cy="6" r="4.5" fill="none" stroke="#1a1a1a" stroke-width="2"/><line x1="9.5" y1="9.5" x2="14" y2="14" stroke="#1a1a1a" stroke-width="2.4"/></svg>
  </div>
  <div class="search-box">
    <svg width="11" height="11" viewBox="0 0 15 15"><circle cx="6" cy="6" r="4.5" fill="none" stroke="#333" stroke-width="2"/><line x1="9.5" y1="9.5" x2="14" y2="14" stroke="#333" stroke-width="2.4"/></svg>
    <span>Enter Keyword</span><b>Search</b>
  </div>

  <div class="video">
    <div class="video-frame" role="img" aria-label="Course preview video frame with the instructor speaking to camera"></div>
    <div class="video-bar">
      <svg width="10" height="12" viewBox="0 0 10 12"><rect x="0" y="0" width="3" height="12" fill="#ddd"/><rect x="6" y="0" width="3" height="12" fill="#ddd"/></svg>
      <span>00:25</span>
      <div class="video-track"><i></i><b></b></div>
      <span>03:33</span>
      <svg width="44" height="12" viewBox="0 0 44 12"><rect x="0" y="2" width="12" height="8" fill="#ddd"/><path d="M18 4h3l4-3v10l-4-3h-3z" fill="#ddd"/><path d="M34 1h4v2M43 1v4M34 11h-1V7M43 11h-4" stroke="#ddd" stroke-width="1.5" fill="none"/></svg>
    </div>
  </div>

  <div class="promo">
    <h1>SIGN UP FOR</h1>
    <p>Mastering Dorvish + Dorvish Nibbles<br>Bundle by Gideon Pell Mawry</p>
  </div>
  <div class="btn-start">
    <svg width="22" height="17" viewBox="0 0 22 17"><path d="M1 2h7c2 0 3 1 3 2.5V16c0-1.2-1-2-3-2H1z M21 2h-7c-2 0-3 1-3 2.5V16c0-1.2 1-2 3-2h7z" fill="none" stroke="#1a1a1a" stroke-width="1.8"/></svg>
    Get Stared
  </div>
</header>

<main>
  <div class="feature-art" style="left:156px;top:709px;background:radial-gradient(circle at 50% 55%,#f4b92a 0%,#f4c64a 28%,#e4e3e1 30%,#e4e3e1 100%)" role="img" aria-label="Illustration of a yellow book with a cartoon pupil"></div>
  <h2 class="feature-title" style="left:462px;top:754px">COURSE INFORMATION</h2>
  <p class="feature-text" style="left:462px;top:802px">Lorem ipsum dolor sit amet, consectetur adipiscing elit. Nulla cursus erat sed dui tincidunt luctusmus viverra nisi in suscipit volutpat. Cras ultricies turpis ac erat facilisis efficitur. Integer ultrices quamsem tempor malesuada. Nunc at lacinia lorem, sed ornare tortor. Nulla facilisi. Aliquam erat volutpatllam felis orci, placerat et tempor vulputate, accumsan vel lectus</p>

  <h2 class="feature-title" style="left:156px;top:1021px">COURSE REVIEWS</h2>
  <p class="feature-text" style="left:156px;top:1069px">Lorem ipsum dolor sit amet, consectetur adipiscing elit. Nulla cursus erat sed dui tincidunt luctusmus viverra nisi in suscipit volutpat. Cras ultricies turpis ac erat facilisis efficitur. Integer ultrices quamsem tempor malesuada. Nunc at lacinia lorem, sed ornare tortor. Nulla facilisi. Aliquam erat volutpatllam felis orci, placerat et tempor vulputate, accumsan vel lectus.</p>
  <div class="feature-art" style="left:787px;top:984px;background:radial-gradient(circle at 50% 50%,#f7f7f7 0%,#eeeeee 30%,#e0dfdd 32%,#e0dfdd 100%)" role="img" aria-label="Illustration of a review document with a pencil"></div>

  <div class="feature-art" style="left:156px;top:1225px;background:radial-gradient(circle at 55% 45%,#5aa7c7 0%,#7fb8c8 28%,#e9e9e4 45%,#d9e5c4 100%)" role="img" aria-label="Illustration of a learner at a computer checking learning progress"></div>
  <h2 class="feature-title" style="left:459px;top:1272px">LEARNING PROGRESS</h2>
  <p class="feature-text" style="left:459px;top:1320px">Lorem ipsum dolor sit amet, consectetur adipiscing elit. Nulla cursus erat sed dui tincidunt luctusmus viverra nisi in suscipit volutpat. Cras ultricies turpis ac erat facilisis efficitur. Integer ultrices quamsem tempor malesuada. Nunc at lacinia lorem, sed ornare tortor. Nulla facilisi. Aliquam erat volutpatllam felis orci, placerat et tempor vulputate, accumsan vel lectus</p>

  <h2 class="feature-title" style="left:156px;top:1550px">STUDY ADVICE</h2>
  <p class="feature-text" style="left:156px;top:1598px">Lorem ipsum dolor sit amet, consectetur adipiscing elit. Nulla cursus erat sed dui tincidunt luctusmus viverra nisi in suscipit volutpat. Cras ultricies turpis ac erat facilisis efficitur. Integer ultrices quamsem tempor malesuada. Nunc at lacinia lorem, sed ornare tortor. Nulla facilisi. Aliquam erat volutpatllam felis orci, placerat et tempor vulputate, accumsan vel lectus.</p>
  <div class="feature-art" style="left:802px;top:1502px;background:radial-gradient(circle at 50% 60%,#2d4d63 0%,#35536a 22%,#8cc7bd 40%,#8cc7bd 100%)" role="img" aria-label="Illustration of a student reading a book"></div>
</main>

<section class="contact">
  <div class="contact-photo" role="img" aria-label="Student writing at a desk in a classroom"></div>
  <div class="contact-veil"></div>
  <h2>CONTACT US</h2>
  <div class="contact-rule"></div>
  <div class="field" style="left:156px;top:89px;width:888px">Your Name</div>
  <div class="field" style="left:156px;top:144px;width:428px">Your Email</div>
  <div class="field" style="left:618px;top:144px;width:426px">Your Phone</div>
  <div class="message">Message</div>
  <div class="btn-send">SEND</div>
</section>

<section class="newsletter">
  <h3>JOIN OUR NEWSLETTER!</h3>
  <p>Sign for a program. <a href="#">Get Our Newsletters!</a></p>
  <div class="news-input">your@email.com</div>
  <div class="news-btn">SUBSCRIBE</div>
</section>

<footer class="footer">
  <div class="footer-links">
    <a class="is-active" href="#">Home</a><span class="sep">/</span><a href="#">About</a><span class="sep">/</span><a href="#">Events</a><span class="sep">/</span><a href="#">Admisions</a><span class="sep">/</span><a href="#">Courses</a><span class="sep">/</span><a href="#">Staff</a><span class="sep">/</span><a href="#">Contact</a>
  </div>
  <div class="copyright">©2015 <b>Vornelle</b>. All Rights Resverd.</div>
  <div class="social" aria-label="Social links">
    <span class="is-active"></span><span></span><span></span><span></span><span></span>
  </div>
</footer>

</body>
</html>
```